GLINT GIN BY TIDE LURE CO

We plan to use a rum product from the caribbean country of Belize CA. That will need to be mentioned somewhere on the label. We want to do a more high-line product, an aged dark rum that plays on the shark theme. We want to use a sleek bottle design with a clever label. Or unique label placement. We need something that will pop off the shelf. We want you to have fun with it and see where it goes. We like the idea of sharks circling around the bottle, possibly like an etching on the glass or back printed on the label or a clear label that can feature the sharks in some capacity. (Not a must) "Chum" because it attracts sharks.

The "Glint Gin" needs a FONT that can become synonymous with the word and then the product. Glint Gin is to be the focus and Tide Lure Co is merely the parent company and requires mention.
Ex:
Tide Lure co.'s Glint Gin
produced in Belize, CA
or Glint Gin produced in Belize for
Tide Lure co.

We have a Glint Gin "mascot" or stamp that is a tribal shark drawing that we want used in the designs where ever you feel fit. We like the stamp as it is, but if you have some tweaks we may consider them.
Updates

I have increased first place to $450.00  and 2nd place to$150.00 !!!

 Everything we have gotten has been great just looking for more ideas. Looking for something sharp and sleek for our bottle we are trying to sell a  upscale rum !! We need it for a aged rum & a white rum .. 

  Thank you !! 
  Torvin

Target Market(s)

MALE 25 TO 45

Industry/Entity Type

It Company

Requirements
Must have
• SHARK THEME ...
Should not have
• OLD WORLD LOOK / MAP LOOKING / TRADITIONAL/ CHEAP.
We don't want everything that has already been done, like all the pirate themes. You can hint at any of these elements in a clever understated way. It is rum after all!

```html
<!DOCTYPE html>
<html lang="en">
<head>
<meta charset="utf-8">
<title>Glint Gin – Label</title>
<link rel="stylesheet" href="https://fonts.googleapis.com/css2?family=Marcellus&family=Philosopher:ital@1&family=Oswald:wght@600&display=swap">
<style>
  :root {
    --paper: #ffffff;
    --pattern-light: #f4f4f4;
    --pattern-mid: #dcdcdc;
    --pattern-dark: #c4c4c4;
    --initial-green: #1d9a5c;
    --title-blue: #1f4596;
    --mascot-red: #ee1c1c;
    --mascot-red-soft: #f7a0a0;
    --info-blue: #23489a;
  }
  html, body {
    margin: 0;
    padding: 0;
    overflow: hidden;
    background: var(--paper);
  }
  .label {
    position: relative;
    width: 1200px;
    height: 681px;
    overflow: hidden;
    background: var(--paper);
  }
  .label__pattern {
    position: absolute;
    inset: 0;
    background:
      repeating-linear-gradient(90deg, var(--pattern-light) 0 60px, var(--pattern-mid) 60px 120px),
      var(--pattern-light);
    background-blend-mode: normal;
    opacity: 0.9;
  }
  .label__pattern::after {
    content: "";
    position: absolute;
    inset: 0;
    background: radial-gradient(circle at 50% 50%, rgba(255,255,255,0.55), rgba(196,196,196,0.35));
  }
  .title-plate {
    position: absolute;
    left: 155px;
    top: 62px;
    width: 980px;
    height: 162px;
    background: var(--paper);
    border-radius: 14px;
  }
  .title {
    position: absolute;
    left: 0;
    top: 0;
    width: 1200px;
    height: 230px;
    margin: 0;
    font-weight: 400;
  }
  .title__word {
    position: absolute;
    top: -30px;
    white-space: nowrap;
    line-height: 1;
  }
  .title__word--first { left: 160px; }
  .title__word--second { left: 735px; }
  .title__initial {
    font-family: "Marcellus", serif;
    color: var(--initial-green);
    font-size: 285px;
  }
  .title__rest {
    font-family: "Philosopher", sans-serif;
    font-style: italic;
    color: var(--title-blue);
    font-size: 190px;
    letter-spacing: 2px;
  }
  .mascot-plate {
    position: absolute;
    left: 250px;
    top: 258px;
    width: 680px;
    height: 232px;
    background: var(--paper);
    border-radius: 24px;
  }
  .mascot {
    position: absolute;
    left: 258px;
    top: 266px;
  }
  .info-plate {
    position: absolute;
    background: var(--paper);
    border-radius: 12px;
  }
  .info-plate--maker {
    left: 130px;
    top: 530px;
    width: 342px;
    height: 160px;
  }
  .info-plate--spec {
    left: 988px;
    top: 540px;
    width: 165px;
    height: 150px;
  }
  .maker {
    position: absolute;
    left: 130px;
    top: 538px;
    width: 342px;
    margin: 0;
    text-align: center;
    font-family: "Oswald", sans-serif;
    font-weight: 600;
    font-size: 38px;
    line-height: 58px;
    color: var(--info-blue);
    text-transform: uppercase;
  }
  .spec {
    position: absolute;
    left: 1012px;
    top: 546px;
    margin: 0;
    padding: 0;
    list-style: none;
    font-family: "Oswald", sans-serif;
    font-weight: 600;
    font-size: 24px;
    line-height: 40px;
    color: var(--info-blue);
    text-transform: uppercase;
  }
</style>
</head>
<body>
  <main class="label">
    <div class="label__pattern" role="img" aria-label="Repeating black and white tribal motif pattern across the label"></div>

    <div class="title-plate"></div>
    <h1 class="title">
      <span class="title__word title__word--first"><span class="title__initial">G</span><span class="title__rest">lint</span></span>
      <span class="title__word title__word--second"><span class="title__initial">G</span><span class="title__rest">in</span></span>
    </h1>

    <div class="mascot-plate"></div>
    <svg class="mascot" width="664" height="216" viewBox="0 0 664 216" role="img" aria-label="Red tribal shark mascot stamp">
      <defs>
        <radialGradient id="mascot-fill" cx="50%" cy="50%" r="60%">
          <stop offset="0" stop-color="var(--mascot-red-soft)"/>
          <stop offset="1" stop-color="var(--mascot-red)"/>
        </radialGradient>
      </defs>
      <rect x="0" y="0" width="664" height="216" rx="20" fill="url(#mascot-fill)"/>
    </svg>

    <div class="info-plate info-plate--maker"></div>
    <p class="maker">Made in Belize<br>for Tide Lure Co.</p>

    <div class="info-plate info-plate--spec"></div>
    <ul class="spec">
      <li>Dry Gin</li>
      <li>80% Proof</li>
      <li>750 ml</li>
    </ul>
  </main>
</body>
</html>
```